Your complete Gardening and lawn maintenance, Horticultural care. (to be on card)
We are looking at using a logo of a tree, with a recycling emblem circling the tree. The colors of choice, are burnt oranges and olive greens. Presented; simple to the eye, yet catchy to the clients in a eco-friendly way. We have uploaded a design for you to look at just to give a rough idea, you can use that or create your own ideas or play around with a mixture.

Target Market(s)

Home owners, businesses, real estates.

Industry/Entity Type

Recycling

Contact Information for Business Card

Name: Colin Breversted
Phone: 0438159027
Email: brightmossyards@mailbarn.net

Logo Text

Bright-Moss Yards

Logo styles of interest
Emblem Logo
Pictorial/Combination Logo
Abstract Logo
Requirements
Must have
• Business name: Bright-Moss Yards
and slogan : Your complete Gardening and lawn maintenance, Horticultural care

```html
<!DOCTYPE html>
<html lang="en">
<head>
<meta charset="utf-8">
<title>Bright-Moss Yards – Business Card</title>
<link rel="stylesheet" href="https://fonts.googleapis.com/css2?family=Roboto+Condensed:wght@300;400;700&display=swap">
<style>
  :root {
    --backdrop: #c8c8c8;
    --card: #ffffff;
    --ink: #1a1a1a;
    --ink-soft: #6b6b6b;
    --ink-muted: #9a9a9a;
    --rule: #8c8c8c;
    --band: #000000;
    --leaf: #7cbf1e;
    --leaf-deep: #5a9a16;
    --ember: #d0661c;
  }
  * { box-sizing: border-box; margin: 0; padding: 0; }
  html, body {
    width: 991px;
    height: 1200px;
    overflow: hidden;
    background: var(--backdrop);
    font-family: "Roboto Condensed", "Arial Narrow", sans-serif;
  }
  .card {
    position: absolute;
    left: 53px;
    width: 885px;
    height: 510px;
    background: var(--card);
    box-shadow: 8px 8px 14px rgba(0, 0, 0, 0.28);
    overflow: hidden;
  }
  .card--green { top: 53px; }
  .card--ember { top: 637px; }

  .divider-vertical {
    position: absolute;
    left: 310px;
    top: 0;
    width: 2px;
    height: 450px;
    background: var(--rule);
  }
  .divider-horizontal {
    position: absolute;
    left: 310px;
    right: 0;
    top: 200px;
    height: 2px;
    background: var(--rule);
  }

  .brand {
    position: absolute;
    left: 0;
    width: 310px;
    top: 140px;
    display: flex;
    flex-direction: column;
    align-items: center;
    gap: 18px;
  }
  .brand-dot {
    width: 84px;
    height: 84px;
    border-radius: 50%;
    background: var(--leaf);
  }
  .card--ember .brand-dot { background: var(--ember); }
  .brand-name {
    font-weight: 700;
    font-size: 27px;
    line-height: 1.05;
    letter-spacing: 0.2px;
    color: var(--leaf);
    text-transform: uppercase;
    text-align: center;
  }

  .person {
    position: absolute;
    left: 373px;
    top: 128px;
    font-weight: 400;
    font-size: 57px;
    line-height: 1;
    color: var(--ink);
    white-space: nowrap;
  }
  .person-surname { color: var(--ink-soft); }
  .card--ember .person-surname { color: var(--ink-muted); }

  .details {
    position: absolute;
    left: 373px;
    top: 210px;
    font-weight: 300;
    font-size: 28px;
    line-height: 43px;
    color: var(--ink-muted);
  }
  .details .role { color: var(--ink-soft); font-weight: 400; }
  .details .at { color: var(--ink-soft); font-weight: 400; }

  .slogan-band {
    position: absolute;
    left: 0;
    right: 0;
    bottom: 0;
    height: 60px;
    background: var(--band);
    color: #ffffff;
    font-weight: 400;
    font-size: 26px;
    display: flex;
    align-items: center;
    justify-content: center;
    white-space: nowrap;
  }
  .slogan-band .accent { color: var(--leaf); }
</style>
</head>
<body>

  <article class="card card--green">
    <div class="divider-vertical"></div>
    <div class="divider-horizontal"></div>
    <div class="brand">
      <span class="brand-dot"></span>
      <span class="brand-name">Bright-Moss<br>Yards</span>
    </div>
    <h1 class="person">Colin <span class="person-surname">Breversted</span></h1>
    <div class="details">
      <p class="role">Marketing Executive</p>
      <p class="email">brightmossyards<span class="at">@</span>mailbarn.net</p>
      <p class="phone">(043)815-9027</p>
    </div>
    <p class="slogan-band">“Your Complete&nbsp;<span class="accent">Gardening</span>,&nbsp;<span class="accent">Lawn</span>&nbsp;Maintenance, and&nbsp;<span class="accent">Horticultural</span>&nbsp;Care”</p>
  </article>

  <article class="card card--ember">
    <div class="divider-vertical"></div>
    <div class="divider-horizontal"></div>
    <div class="brand">
      <span class="brand-dot"></span>
      <span class="brand-name">Bright-Moss<br>Yards</span>
    </div>
    <h1 class="person">Colin <span class="person-surname">Breversted</span></h1>
    <div class="details">
      <p class="role">Marketing Executive</p>
      <p class="email">brightmossyards<span class="at">@</span>mailbarn.net</p>
      <p class="phone">(043)815-9027</p>
    </div>
    <p class="slogan-band">“Your Complete&nbsp;<span class="accent">Gardening</span>,&nbsp;<span class="accent">Lawn</span>&nbsp;Maintenance, and&nbsp;<span class="accent">Horticultural</span>&nbsp;Care”</p>
  </article>

</body>
</html>
```